I would like a stylish low key card that represents my Cedar Nook. A boutique rental property . This property is of the highest standard and I wish the card to covey this without being old fashion

Boutique

Tessa Varrow
0427350192
tessa.varrow@varrow.com.au Cedar Nook

```html
<!DOCTYPE html>
<html lang="en">
<head>
<meta charset="utf-8">
<title>Cedar Nook – Business Card</title>
<link rel="stylesheet" href="https://fonts.googleapis.com/css2?family=Barlow:wght@300;400;600&display=swap">
<style>
  :root {
    --backdrop: #ecebea;
    --card: #2f3133;
    --card-texture: #34373a;
    --panel: #3a3d40;
    --text-strong: #f2f2f2;
    --text-soft: #c9cbcd;
    --brand: #d4d6d8;
  }
  * { box-sizing: border-box; margin: 0; padding: 0; }
  html, body {
    width: 1200px;
    height: 741px;
    overflow: hidden;
    background: var(--backdrop);
  }
  .stage {
    position: relative;
    width: 1200px;
    height: 741px;
  }
  .card {
    position: absolute;
    left: 140px;
    top: 100px;
    width: 920px;
    height: 540px;
    background: var(--card);
    border-radius: 4px;
    box-shadow: 0 18px 40px rgba(0,0,0,0.22);
    overflow: hidden;
  }
  .card__texture {
    position: absolute;
    inset: 0;
    background: linear-gradient(135deg, var(--card-texture), var(--card));
  }
  .card__panel {
    position: absolute;
    left: 470px;
    top: 92px;
    right: 36px;
    bottom: 36px;
    background: var(--panel);
    padding: 34px 30px 0 30px;
    font-family: "Barlow", "Helvetica Neue", Arial, sans-serif;
    white-space: nowrap;
  }
  .contact__line {
    display: flex;
    justify-content: space-between;
    align-items: baseline;
    gap: 24px;
  }
  .contact__name {
    font-weight: 600;
    font-size: 22px;
    letter-spacing: 1.5px;
    text-transform: uppercase;
    color: var(--text-strong);
  }
  .contact__phone {
    font-weight: 400;
    font-size: 22px;
    letter-spacing: 1px;
    color: var(--text-soft);
  }
  .contact__email {
    margin-top: 8px;
    font-weight: 300;
    font-size: 22px;
    letter-spacing: 0.6px;
    color: var(--text-soft);
  }
  .brand {
    position: absolute;
    left: 30px;
    right: 30px;
    bottom: 36px;
    font-weight: 300;
    font-size: 66px;
    line-height: 1;
    letter-spacing: -0.5px;
    color: var(--brand);
  }
</style>
</head>
<body>
  <main class="stage">
    <article class="card">
      <div class="card__texture" role="img" aria-label="Subtle tonal cross pattern across the card background"></div>
      <section class="card__panel">
        <div class="contact">
          <p class="contact__line">
            <span class="contact__name">Tessa Varrow</span>
            <span class="contact__phone">042 735 01 92</span>
          </p>
          <p class="contact__email">tessa.varrow@varrow.com.au</p>
        </div>
        <p class="brand">Cedar Nook</p>
      </section>
    </article>
  </main>
</body>
</html>
```